Kestrel Lending, Inc. trade show retractible banner

We are a small mortgage broker in Colorado. We have been in business since 1996 and offer Conventional, FHA, VA, USDA and reverse mortgages for both purchase and refinance. Our business is primarily repeat and referral business, but we do some trade shows and events. Our web sites are www.KestrelLendingInc.example and www.KestrelLending.example Phone numbers 303-555-0187 or 800-555-0142. We are located at 10890 Pelham Blvd, Broomfield, CO 80021 I am looking for a design that will fit the parameters of a 24" x 40: Table top Retractable Banner Stand from QVL Displays, http://www.qvldisplays.example/economy-24-x-40-table-top-retractable-banner-stand My goal is a table top banker that will cause people to stop at our table in a trade show and engage in a conversation. The best reason to stop would be for the banner to trigger a question from the participant as they walk by. The question could relate to a home purchase, a refinance, or a reverse mortgage. It could be about a primary residence, second home, or investment property located in Colorado. Design should convey that we are a local trusted company. We are A+ rated with the CTB. We have been selected as Summit Peak Review Leading Loan Advisors in 2011, 2012, and 2014. I am Colorado Licensed Mortgage Loan Originator 100004213 LRCR #738264 I have uploaded a logo in .ai file format. Contact me with questions at Walt@KestrelLendingInc.example This is my first try at using this service.

Target Market(s)

Adults, homeowners or prospective homeowners, typical 30-70 age, male or female

Industry/Entity Type

Investment

Requirements
Must have
• Choose colors compatible with our logo The logo colors are Blue Kestrel Lending is supposed to be PMS 288 and the stars are supposed to be a 20% screen of Pantone Cool Gray I sent the ai file of the logo because it is high resolution. The JPG should have the correct colors.
Nice to have
• Picture of happy people with a home.
Should not have
• Reference to pricing

```html
<!DOCTYPE html>
<html lang="en">
<head>
<meta charset="utf-8">
<title>Kestrel Lending, Inc. — Table Top Banner</title>
<link rel="stylesheet" href="https://fonts.googleapis.com/css2?family=Noto+Serif:wght@400;700&family=Arimo:ital,wght@1,400;1,700&display=swap">
<style>
  :root {
    --backdrop: #ececec;
    --banner-blue: #124b8c;
    --banner-red: #d11f2a;
    --paper: #ffffff;
    --ink: #111111;
    --logo-blue: #1b3f8f;
    --contact-blue: #1d4f9c;
    --photo-top: #e2d9c8;
    --photo-mid: #cdbfa8;
    --photo-bottom: #9a8f80;
    --badge-dark: #0d0d0d;
  }
  * { box-sizing: border-box; margin: 0; padding: 0; }
  html, body {
    width: 1000px; height: 1200px; overflow: hidden;
    background: var(--backdrop);
  }
  .banner {
    position: absolute; left: 170px; top: 51px;
    width: 660px; height: 1098px;
    display: flex; flex-direction: column;
    font-family: "Noto Serif", Georgia, serif;
  }
  .services {
    height: 290px; background: var(--banner-blue);
    padding: 62px 0 0 32px;
    color: #fff; font-weight: 700; font-size: 49px;
    line-height: 61px; letter-spacing: -1.6px;
  }
  .hero-photo {
    height: 440px;
    background: linear-gradient(180deg, var(--photo-top) 0%, var(--photo-mid) 60%, var(--photo-bottom) 100%);
  }
  .tagline {
    height: 164px; background: var(--banner-red);
    padding: 26px 0 0 31px;
    color: #fff; font-weight: 700; font-size: 55px; line-height: 56px;
    text-shadow: 2px 2px 3px rgba(0,0,0,.35);
  }
  .tagline .line-one { word-spacing: 14px; }
  .tagline .line-two { letter-spacing: 9px; }
  .footer {
    flex: 1; background: var(--paper); position: relative;
  }
  .license {
    position: absolute; left: 29px; top: 8px;
    font-weight: 700; font-size: 15.5px; color: var(--ink);
    white-space: nowrap;
  }
  .brand {
    position: absolute; left: 30px; top: 88px; width: 214px;
    text-align: center; color: var(--logo-blue); white-space: nowrap;
  }
  .brand-name { font-size: 20px; font-weight: 400; line-height: 26px; }
  .brand-since { font-size: 12px; margin-top: 2px; font-style: italic; }
  .divider {
    position: absolute; left: 253px; top: 76px;
    width: 1px; height: 74px; background: var(--logo-blue);
  }
  .contact {
    position: absolute; left: 268px; top: 74px;
    font-family: "Arimo", Arial, sans-serif; font-style: italic;
    font-size: 13.5px; line-height: 17px; color: var(--contact-blue);
  }
  .contact .phone { font-weight: 700; }
  .accreditation-badge {
    position: absolute; left: 450px; top: 40px;
    width: 169px; height: 64px; border-radius: 6px;
    background: var(--badge-dark);
  }
  .award {
    position: absolute; left: 440px; top: 114px; width: 189px;
    text-align: center; color: var(--ink); font-weight: 700;
    white-space: nowrap;
  }
  .award-name { font-size: 18px; line-height: 24px; }
  .award-title { font-size: 11px; line-height: 15px; }
</style>
</head>
<body>
  <main class="banner">
    <section class="services">
      <p>home purchase ...</p>
      <p>refinance ...</p>
      <p>reverse mortgage ...</p>
    </section>
    <div class="hero-photo" role="img" aria-label="Photo of a smiling family of three standing in front of the porch of their home"></div>
    <section class="tagline">
      <p class="line-one">We have the</p>
      <p class="line-two">ANSWERS</p>
    </section>
    <footer class="footer">
      <p class="license">Colorado Licensed Mortgage Loan Originator 100004213 LRCR #738264</p>
      <div class="brand">
        <p class="brand-name">Kestrel Lending, Inc.</p>
        <p class="brand-since">Since 1996</p>
      </div>
      <div class="divider"></div>
      <address class="contact">
        <span class="phone">303.555.0187</span><br>
        <span class="phone">800.555.0142</span><br>
        10890 Pelham Blvd.,<br>
        Broomfield, CO 80021
      </address>
      <div class="accreditation-badge" role="img" aria-label="CTB accredited business badge"></div>
      <div class="award">
        <p class="award-name">Summit Peak Review</p>
        <p class="award-title">Leading Loan Advisors</p>
      </div>
    </footer>
  </main>
</body>
</html>
```